Business Card design for shipping company 'FARNHOLT MARITIME LTD'

Classic / traditional business card in black Garamond / Times New Roman or similar text for a shipping / marine transport company, containing the following information:

QUOTE

FARNHOLT MARITIME LTD

PETER CALLOWAY FICS

T: +44 7923 615087
E: vessels@farnholt-mar.com

UNQUOTE

Target Market(s)

Marine / Shipping industry

Contact Information for Business Card

FARNHOLT MARITIME LTD PETER CALLOWAY FICS T: +44 7923 615087 E: vessels@farnholt-mar.com

Font styles to use
Serif

Colors

Designer to choose colors to be used in the design.

Requirements
Must have
• Garamond / Times New Roman or similar text in black colour

```html
<!DOCTYPE html>
<html lang="en">
<head>
<meta charset="utf-8">
<title>Farnholt Maritime Ltd — Business Card</title>
<link href="https://fonts.googleapis.com/css2?family=EB+Garamond:wght@400;600&display=swap" rel="stylesheet">
<style>
  :root {
    --backdrop: #d0cfd0;
    --card: #16161d;
    --ink: #ffffff;
    --ink-soft: #d9d9de;
    --rule: #8a8a92;
  }
  * { margin: 0; padding: 0; box-sizing: border-box; }
  html, body {
    width: 1200px; height: 1200px; overflow: hidden;
    background: var(--backdrop);
  }
  .sheet {
    width: 1200px; height: 1200px;
    display: flex; flex-direction: column; align-items: center; justify-content: center;
    gap: 60px;
  }
  .card {
    position: relative;
    width: 900px; height: 514px;
    background: var(--card);
    color: var(--ink);
    font-family: "EB Garamond", "Times New Roman", serif;
  }
  .wordmark {
    position: absolute;
    text-align: center;
    font-weight: 600;
    line-height: 1;
  }
  .wordmark__main { display: block; font-size: 46px; letter-spacing: 4px; }
  .wordmark__sub { display: block; font-size: 23px; letter-spacing: 3.5px; margin-top: 4px; color: var(--ink-soft); }
  .card--front .wordmark { left: 0; right: 0; top: 212px; }
  .card--back .wordmark { left: 80px; width: 420px; top: 300px; }
  .divider {
    position: absolute; left: 520px; top: 140px;
    width: 1px; height: 210px; background: var(--rule);
  }
  .contact { position: absolute; left: 550px; top: 145px; }
  .contact__name { font-size: 24px; font-weight: 600; letter-spacing: 0.5px; }
  .contact__role { font-size: 22px; color: var(--ink-soft); margin-top: 2px; }
  .contact__list { list-style: none; margin-top: 38px; }
  .contact__item {
    display: flex; align-items: center; gap: 14px;
    font-size: 23px; letter-spacing: 0.5px; margin-bottom: 26px;
  }
  .contact__icon { width: 30px; height: 30px; flex: none; }
</style>
</head>
<body>
<main class="sheet">
  <section class="card card--front">
    <div class="wordmark">
      <span class="wordmark__main">FARNHOLT</span>
      <span class="wordmark__sub">MARITIME LTD</span>
    </div>
  </section>

  <section class="card card--back">
    <div class="wordmark">
      <span class="wordmark__main">FARNHOLT</span>
      <span class="wordmark__sub">MARITIME LTD</span>
    </div>
    <div class="divider"></div>
    <div class="contact">
      <div class="contact__name">PETER CALLOWAY FICS</div>
      <div class="contact__role">Director</div>
      <ul class="contact__list">
        <li class="contact__item">
          <svg class="contact__icon" viewBox="0 0 30 30" aria-hidden="true">
            <circle cx="15" cy="15" r="15" fill="#ffffff"/>
            <path d="M10 8.5c1-.6 2-.3 2.5.6l1.2 2.2c.4.8.2 1.5-.5 2l-.9.6c.8 1.8 2 3 3.8 3.8l.6-.9c.5-.7 1.2-.9 2-.5l2.2 1.2c.9.5 1.2 1.5.6 2.5-.8 1.3-2.2 1.9-3.6 1.5-4.2-1.3-7.3-4.4-8.6-8.6-.4-1.4.2-2.8 1.7-3.9z" fill="#16161d"/>
          </svg>
          <span>+44 7923 615087</span>
        </li>
        <li class="contact__item">
          <svg class="contact__icon" viewBox="0 0 30 30" aria-hidden="true">
            <circle cx="15" cy="15" r="15" fill="#ffffff"/>
            <rect x="8" y="10" width="14" height="10" rx="1" fill="none" stroke="#16161d" stroke-width="1.6"/>
            <path d="M8.5 10.5l6.5 5 6.5-5" fill="none" stroke="#16161d" stroke-width="1.6"/>
          </svg>
          <span>vessels@farnholt-mar.com</span>
        </li>
      </ul>
    </div>
  </section>
</main>
</body>
</html>
```